Wren Vehicle Polishing (Mobile detail)

I need a business card made up. I'd like it to be different in some form, either raised, embossed, debossed, something cool that stands out. (preferably embossed text somewhere in it). I will be including the Initial png file. Let me know if you need the photoshop of adobe illustrator file to work with.

Information to be included: Text: XXX-XXX-XXXX Phone: XXX-XXX-XXXX Email: wrenpolishcrew@mailbox-demo.net Website: www.socialpage-demo.net/wrenpolishKTR Hours of operation: Mon - Fri 7:00AM to 8:00PM Sat - 10:00AM to 8:00PM

Target Market(s)

Mobile automotive detailing

Industry/Entity Type

Automotive

Contact Information for Business Card

Make it stand out with embossed lettering, I'd also like the background to be glossy black or matte, something that represents a shiny car, black preferred

Requirements
Must have
• A glossy background, or something.
• My logo, pick one of them that best fits your design.
Should not have
• White background,
• something that does not stand out.

```html
<!DOCTYPE html>
<html lang="en">
<head>
<meta charset="utf-8">
<title>Wren Vehicle Polishing – Business Card</title>
<link href="https://fonts.googleapis.com/css2?family=Libre+Baskerville:wght@700&family=Roboto:wght@400;500;700&display=swap" rel="stylesheet">
<style>
  :root {
    --backdrop: #e9e6e1;
    --orange-light: #f29a3f;
    --orange-deep: #e0731c;
    --gloss-black: #0b0b0b;
    --black-sheen: #262626;
    --edge-white: #f4f4f4;
    --text-white: #f2f2f2;
    --text-dark: #161616;
    --accent: #f08a24;
  }
  * { margin: 0; padding: 0; box-sizing: border-box; }
  html, body {
    width: 1200px; height: 1022px; overflow: hidden;
    background: var(--backdrop);
  }
  .business-card {
    position: absolute; left: 100px; top: 225px;
    width: 1000px; height: 572px;
    border-radius: 22px; overflow: hidden;
    background: linear-gradient(135deg, var(--orange-light), var(--orange-deep));
    box-shadow: 0 14px 34px rgba(0,0,0,.28);
  }
  .card-shape { position: absolute; inset: 0; width: 100%; height: 100%; }
  .holder-name {
    position: absolute; right: 56px; top: 42px; text-align: right;
    font-family: "Libre Baskerville", Georgia, serif; font-weight: 700;
    font-size: 36px; letter-spacing: 1px; color: var(--text-dark);
  }
  .holder-role {
    display: block; margin-top: 6px;
    font-family: "Roboto", Arial, sans-serif; font-weight: 400;
    font-size: 19px; letter-spacing: 1px; color: var(--text-white);
  }
  .brand-mark {
    position: absolute; left: 70px; top: 140px; width: 360px;
    display: flex; align-items: center; gap: 18px;
  }
  .brand-dot {
    flex: none; width: 58px; height: 58px; border-radius: 50%;
    background: var(--gloss-black);
  }
  .brand-name {
    font-family: "Roboto", Arial, sans-serif; font-weight: 700;
    font-size: 34px; line-height: 1.15; color: var(--text-dark);
  }
  .opening-hours {
    position: absolute; left: 58px; bottom: 46px;
    font-family: "Roboto", Arial, sans-serif; color: var(--text-white);
    font-size: 22px; line-height: 1.4;
  }
  .opening-hours h2 {
    font-size: 23px; font-weight: 500; color: var(--accent); letter-spacing: .5px;
  }
  .contact-list {
    position: absolute; right: 52px; bottom: 60px; list-style: none;
    font-family: "Roboto", Arial, sans-serif; font-size: 22px; line-height: 1.45;
    color: var(--text-white); text-align: right;
  }
  .contact-list li { display: flex; justify-content: flex-end; align-items: center; gap: 14px; }
  .contact-icon { width: 18px; height: 18px; flex: none; }
</style>
</head>
<body>
  <article class="business-card">
    <svg class="card-shape" viewBox="0 0 1000 572" preserveAspectRatio="none" aria-hidden="true">
      <defs>
        <linearGradient id="blackGloss" x1="0" y1="0" x2="1" y2="1">
          <stop offset="0" stop-color="var(--black-sheen)"/>
          <stop offset=".45" stop-color="var(--gloss-black)"/>
          <stop offset="1" stop-color="#151515"/>
        </linearGradient>
      </defs>
      <path d="M0,572 L0,395 C200,390 360,160 640,160 C810,160 900,150 1000,140 L1000,572 Z"
            fill="url(#blackGloss)"/>
      <path d="M0,395 C200,390 360,160 640,160 C810,160 900,150 1000,140"
            fill="none" stroke="var(--edge-white)" stroke-width="5"/>
    </svg>

    <h1 class="holder-name">MARLO KESSING<span class="holder-role">DIRECTOR</span></h1>

    <div class="brand-mark">
      <span class="brand-dot"></span>
      <span class="brand-name">Wren Vehicle Polishing</span>
    </div>

    <section class="opening-hours">
      <h2>HOURS OF OPERATION:</h2>
      <p>Mon - Fri 7:00AM to 8:00PM</p>
      <p>Sat - 10:00AM to 8:00PM</p>
    </section>

    <ul class="contact-list">
      <li>XXX-XXX-XXXX
        <svg class="contact-icon" viewBox="0 0 18 18"><rect x="4" y="1" width="10" height="16" rx="2" fill="none" stroke="var(--accent)" stroke-width="2"/></svg></li>
      <li>XXX-XXX-XXXX
        <svg class="contact-icon" viewBox="0 0 18 18"><path d="M4 2l3 0 1.5 4-2 1.5a9 9 0 0 0 4 4L12 9.5l4 1.5v3a2 2 0 0 1-2 2A13 13 0 0 1 2 4a2 2 0 0 1 2-2z" fill="var(--accent)"/></svg></li>
      <li>wrenpolishcrew@mailbox-demo.net
        <svg class="contact-icon" viewBox="0 0 18 18"><rect x="1" y="4" width="16" height="11" fill="none" stroke="var(--accent)" stroke-width="2"/><path d="M1 4l8 6 8-6" fill="none" stroke="var(--accent)" stroke-width="2"/></svg></li>
      <li>www.socialpage-demo.net/wrenpolishKTR
        <svg class="contact-icon" viewBox="0 0 18 18"><circle cx="9" cy="9" r="7" fill="none" stroke="var(--accent)" stroke-width="2"/><path d="M2 9h14M9 2c3 3 3 11 0 14M9 2c-3 3-3 11 0 14" fill="none" stroke="var(--accent)" stroke-width="1.5"/></svg></li>
    </ul>
  </article>
</body>
</html>
```